Business Broker Graphics Package

Hi,

Seeking a smart and professional graphics package design including business card design (double-sided) and letterhead and PowerPoint slide template.

3 Deliverables:

1. Company Letterhead
2. Business Card (two sided) (will consider one sided designs)
3. PowerPoint Template. Requires cover PPT and 2nd page design.

For the prototype use this info:
Harold Brunsky QRN
Certified Business Intermediary
5821 Larkfield Rd.
Tampa, FL 77777
555.314.2768
Sample@Corvelloplace.com
www.CorvelloPlace.com

I'll give exact information to winner to finalize later.

I've attached the logo..

Business card will be double sided and info for back of card is in attachment.

Look forward to your great ideas and concepts!

Project Deadline Extended
Reason: Just finalized logo design so now I'm ready to proceed with graphics package. Thanks!

Project Deadline Extended
Reason: More time to complete work! Thanks!

Target Market(s)

President's and business owners, CPA's and other professionals.

Industry/Entity Type

Business

Requirements
Nice to have
• Prefer horizontal card, but will consider vertical card design.

The business card should be all or primarily white. Text colors should be same as logo creative combination of black and forest green.

PowerPoint can be white background or lighter palette of colors I like gold color. I do not like darkly colored PowerPoint designs I prefer light and bright designs.

```html
<!DOCTYPE html>
<html lang="en">
<head>
<meta charset="utf-8">
<title>Corvello Place Letterhead Designs</title>
<link rel="stylesheet" href="https://fonts.googleapis.com/css2?family=Cinzel:wght@600&family=Montserrat:wght@300;400;500;700&display=swap">
<style>
  :root {
    --board: #efefef;
    --paper: #ffffff;
    --paper-shade: #e4e4e4;
    --ink: #111111;
    --muted: #7b7b7b;
    --forest: #046836;
    --header-grey: #d9d9d9;
    --ghost: rgba(0, 0, 0, 0.07);
  }
  * { margin: 0; padding: 0; box-sizing: border-box; }
  html, body { width: 1200px; height: 1000px; overflow: hidden; }
  body {
    position: relative;
    background: var(--board);
    font-family: "Montserrat", Arial, sans-serif;
    color: var(--ink);
  }
  .board-title {
    position: absolute; top: 38px; left: 0; width: 1200px;
    text-align: center; font-size: 31px; letter-spacing: 0.5px;
    font-weight: 300; color: var(--muted);
  }
  .board-title strong { font-weight: 700; color: var(--forest); }

  .sheet {
    position: absolute; top: 165px; width: 520px; height: 735px;
    overflow: hidden;
    background: linear-gradient(180deg, var(--paper) 0%, #f2f2f2 45%, var(--paper-shade) 100%);
    box-shadow: 4px 5px 6px rgba(0, 0, 0, 0.35);
  }
  .sheet--classic { left: 57px; }
  .sheet--banded { left: 617px; }

  .brand {
    position: absolute; top: 52px; left: 0; width: 100%;
    text-align: center;
  }
  .brand-name {
    font-family: "Cinzel", Georgia, serif; font-weight: 600;
    font-size: 21px; color: var(--ink); letter-spacing: 0.3px; line-height: 1;
  }
  .brand-tagline {
    font-family: "Cinzel", Georgia, serif; font-weight: 600;
    font-size: 7.5px; color: var(--ink); margin-top: 3px;
  }

  .salutation { position: absolute; top: 182px; left: 36px; }
  .salutation-line { font-size: 13.5px; font-weight: 500; }
  .salutation-note { font-size: 10px; font-weight: 400; color: #333; margin-top: 1px; }

  .ghost-name {
    position: absolute; left: 28px; top: 618px;
    font-family: "Cinzel", Georgia, serif; font-weight: 600;
    font-size: 82px; color: var(--ghost); white-space: nowrap;
    transform: rotate(-4deg); transform-origin: left top;
  }
  .footer-rule {
    position: absolute; left: 38px; top: 690px; width: 480px;
    border-top: 1px solid rgba(0, 0, 0, 0.25);
  }
  .contact {
    position: absolute; left: 0; width: 100%; text-align: center;
    font-size: 7.5px; line-height: 9.5px; font-weight: 500; color: var(--ink);
  }
  .contact-title { margin-bottom: 9px; }
  .sheet--classic .contact { top: 676px; left: 100px; width: 320px; }

  .header-band {
    position: absolute; top: 0; left: 0; width: 100%; height: 112px;
    background: var(--header-grey);
    border-bottom: 4px solid var(--forest);
  }
  .pattern-field {
    position: absolute; top: 116px; left: 0; width: 100%; height: 549px;
    background: repeating-linear-gradient(180deg, rgba(0,0,0,0.035) 0 40px, transparent 40px 80px),
                linear-gradient(180deg, #f4f4f4, #e8e8e8);
  }
  .footer-band {
    position: absolute; bottom: 0; left: 0; width: 100%; height: 70px;
    background: var(--forest);
  }
  .sheet--banded .contact { top: 675px; color: #ffffff; }
</style>
</head>
<body>
  <h1 class="board-title">LETTERHEAD<strong>DESIGNS</strong></h1>

  <section class="sheet sheet--classic">
    <div class="brand">
      <div class="brand-name">CorvelloPlace</div>
      <div class="brand-tagline">Merger Acquisition Growth Experts</div>
    </div>
    <div class="salutation">
      <p class="salutation-line">To whom this letter may concern</p>
      <p class="salutation-note">Please carefully read and respond accordingly</p>
    </div>
    <div class="ghost-name" aria-hidden="true">CORVELLO</div>
    <div class="footer-rule"></div>
    <div class="contact">
      <p class="contact-title">Corvello Place: Merger Acquisitions Growth Experts</p>
      <p>Address: 5821 Larkfield Rd. Tampa, FL Postal Code 77777</p>
      <p>555.314.2768 - Sample@Corvelloplace.com</p>
      <p>www.CorvelloPlace.com</p>
    </div>
  </section>

  <section class="sheet sheet--banded">
    <div class="header-band"></div>
    <div class="brand">
      <div class="brand-name">CorvelloPlace</div>
      <div class="brand-tagline">Merger Acquisition Growth Experts</div>
    </div>
    <div class="pattern-field" role="img" aria-label="Faint repeating pattern of the company name across the letter body"></div>
    <div class="salutation">
      <p class="salutation-line">To whom this letter may concern</p>
      <p class="salutation-note">Please carefully read and respond accordingly</p>
    </div>
    <div class="footer-band"></div>
    <div class="contact">
      <p class="contact-title">Corvello Place: Merger Acquisitions Growth Experts</p>
      <p>Address: 5821 Larkfield Rd. Tampa, FL Postal Code 77777</p>
      <p>555.314.2768 - Sample@Corvelloplace.com</p>
      <p>www.CorvelloPlace.com</p>
    </div>
  </section>
</body>
</html>
```